Harborline Estates Business Card for Apartment Buildings

Create business cards for resident managers who run apartment buildings. The audience is the public who are searching for apartment rentals, and current residents who live at the apartment building. Key design element will be incorporating the company logo, however, the logo cannot dominate. The building name and manager name are more important than the logo. Current business card design leaves little room for copy, so we may need to reduce the size on the current card to allow for more space for copy.

Target Market(s)

Adults 18-65 years of age, who are looking for an apartment rental, plus current residents who live at our apartment buildings.

Industry/Entity Type

Property Management

Contact Information for Business Card

A major design element will be use of the company logo. Important property and manager contact information must be part of the design. The size of the logo will need to be reduced to make room for building and manager contact copy.

Font styles to use
Sans Serif

Colors
3176b5
000000
959595
ffffff

Requirements
Must have
• 1) Incorporate the company logo.
• 2) Use the company colors (dark blue, black/grey, over white).
• 3) FEATURE THE BUILDING NAME
• 4) FEATURE THE MANAGER NAME
• 5) The company name is less important than BUILDING and MANAGER
• 6) Manager contact information
• **SEE ATTACHED CREATIVE BRIEF**
Nice to have
• 1) Back of card logo watermark
• 2) Ability to write notes on back of carfd
Should not have
• Avoid letting the company logo dominate the card, the building name and manager are more important than the company logo.

```html
<!DOCTYPE html>
<html lang="en">
<head>
<meta charset="utf-8">
<title>Harborline Estates Business Card</title>
<link href="https://fonts.googleapis.com/css2?family=Source+Sans+3:wght@400;600;700&display=swap" rel="stylesheet">
<style>
  :root {
    --brand-blue: #3176b5;
    --ink-black: #000000;
    --stone-grey: #959595;
    --shadow-grey: #7f7f7f;
    --paper-white: #ffffff;
    --backdrop: #f2f2f2;
  }
  * { box-sizing: border-box; margin: 0; padding: 0; }
  html, body {
    width: 1200px;
    height: 1200px;
    overflow: hidden;
    background: var(--backdrop);
    font-family: "Source Sans 3", sans-serif;
  }
  .canvas { position: relative; width: 1200px; height: 1200px; }

  .card {
    position: absolute;
    left: 221px;
    width: 758px;
    height: 433px;
    overflow: hidden;
  }
  .card-front { top: 100px; background: var(--ink-black); }
  .card-back { top: 665px; background: var(--paper-white); }

  .front-shapes { position: absolute; inset: 0; width: 100%; height: 100%; }

  .brand {
    position: absolute;
    left: 500px;
    top: 34px;
    display: flex;
    align-items: center;
    gap: 10px;
    color: var(--paper-white);
    font-weight: 700;
    font-size: 22px;
    line-height: 1.02;
    letter-spacing: 0.5px;
    text-transform: uppercase;
  }
  .brand-dot {
    width: 40px;
    height: 40px;
    border-radius: 50%;
    background: var(--paper-white);
    flex: none;
  }

  .web-address {
    position: absolute;
    left: 50px;
    top: 76px;
    color: var(--paper-white);
    font-size: 15px;
  }

  .name-accent {
    position: absolute;
    left: 0;
    top: 142px;
    width: 18px;
    height: 48px;
    background: var(--brand-blue);
  }
  .manager-name {
    position: absolute;
    left: 49px;
    top: 135px;
    color: var(--brand-blue);
    font-size: 27px;
    font-weight: 700;
    letter-spacing: 0.3px;
  }
  .manager-title {
    position: absolute;
    left: 49px;
    top: 168px;
    color: var(--paper-white);
    font-size: 17px;
  }

  .contact-block {
    position: absolute;
    left: 49px;
    top: 218px;
    color: var(--paper-white);
    font-size: 19px;
    line-height: 25.2px;
    list-style: none;
    text-transform: uppercase;
  }

  .back-band {
    position: absolute;
    left: 0; top: 0;
    width: 100%;
    height: 132px;
    background: var(--ink-black);
    display: flex;
    align-items: center;
    justify-content: center;
    color: var(--paper-white);
    font-size: 19px;
  }
  .note-line {
    position: absolute;
    left: 72px;
    width: 614px;
    height: 3px;
    background: var(--stone-grey);
  }
</style>
</head>
<body>
<main class="canvas">

  <section class="card card-front" aria-label="Business card front">
    <svg class="front-shapes" viewBox="0 0 632 361" preserveAspectRatio="none" aria-hidden="true">
      <polygon points="324,0 632,0 632,361 495,197" fill="var(--brand-blue)"/>
      <polygon points="404,361 495,197 632,361" fill="var(--shadow-grey)"/>
      <polygon points="404,361 490,215 619,361" fill="var(--stone-grey)"/>
    </svg>

    <div class="brand">
      <span class="brand-dot"></span>
      <span class="brand-name">Harborline<br>Estates</span>
    </div>

    <p class="web-address">www.harborlineestates.us</p>

    <span class="name-accent"></span>
    <h1 class="manager-name">MARISOL QUINTERO</h1>
    <p class="manager-title">RESIDENT MANAGER</p>

    <ul class="contact-block">
      <li class="building-name">Bayview Court Apartments</li>
      <li>2480 Cedar Row</li>
      <li>Port Alder, CA 92140</li>
      <li>Office: 555-210-4830</li>
      <li>Fax: 555-210-4831</li>
      <li>Cell: 555-386-9172</li>
      <li>Email: marisol@harborlinehq.com</li>
    </ul>
  </section>

  <section class="card card-back" aria-label="Business card back">
    <div class="back-band">www.harborlineestates.us</div>
    <span class="note-line" style="top:168px"></span>
    <span class="note-line" style="top:213px"></span>
    <span class="note-line" style="top:258px"></span>
    <span class="note-line" style="top:302px"></span>
    <span class="note-line" style="top:347px"></span>
    <span class="note-line" style="top:392px"></span>
  </section>

</main>
</body>
</html>
```